Business card for Eyelash extension salon in Alder Vale,California USA

We need new business card for our salon in Alder Vale. The salon name is 'Lumarra' . We would like to have...Business name: Lumarra Name of person: will provide later Address 6128 N.Corbel Ridge Blvd Alder Vale , AV 00417 Phone: will provide later (Text only) Web: www.lumarrastudio-example.com Pictogrid icon, Friendvale icon follow us for seasonal campaign and news @lumarrastudioexample Design should look elegant, high-end, clean, simple, cohesive with my brand. Please refer my brand board. Business name color will be metallic bronzy color. Im thinking grey background or white background. Thanks

Target Market(s)

25-35. Gender neutral. People who are in Entertainment business industry.
This is High-end Eyelash extension salon in Alder Vale

Industry/Entity Type

Beauty Salon

Contact Information for Business Card

Business name: Lumarra
Name of person: will provide later
Address 6128 N.Corbel Ridge Blvd Alder Vale , AV 00417
Phone: will provide later (Text only)
Web: www.lumarrastudio-example.com
Pictogrid icon, Friendvale icon
follow us for seasonal campaign and news @lumarrastudioexample

Requirements
Must have
• Beautiful, elegant, clean and simple look but very attractive and modern
Should not have
• We don't like too clutter, too busy designs.

```html
<!DOCTYPE html>
<html lang="en">
<head>
<meta charset="utf-8">
<title>Lumarra Business Card</title>
<link rel="stylesheet" href="https://fonts.googleapis.com/css2?family=Playfair+Display:wght@400;700&family=Questrial&display=swap">
<style>
  :root {
    --stage: #424040;
    --sand: #c9ab8a;
    --cream: #ead9c8;
    --bronze: #5b3e2d;
    --bronze-soft: #d2b593;
    --white: #ffffff;
  }
  * { margin: 0; padding: 0; box-sizing: border-box; }
  html, body { width: 1006px; height: 1200px; overflow: hidden; }
  body {
    background: var(--stage);
    font-family: "Questrial", sans-serif;
    position: relative;
  }
  .card {
    position: absolute;
    left: 73px;
    width: 860px;
    height: 516px;
    overflow: hidden;
  }
  .card--front { top: 56px; background: var(--sand); }
  .card--back { top: 628px; background: var(--cream); }

  .wordmark {
    position: absolute;
    text-align: center;
    font-family: "Playfair Display", serif;
    font-weight: 400;
    line-height: 1;
  }
  .wordmark__name { display: block; font-size: 84px; letter-spacing: 1px; }
  .wordmark__place {
    display: block;
    margin-top: 8px;
    font-family: "Questrial", sans-serif;
    font-size: 11px;
    letter-spacing: 3px;
  }
  .card--front .wordmark { left: 0; right: 0; top: 200px; color: var(--white); }
  .card--back .wordmark { left: 80px; width: 300px; top: 170px; color: var(--bronze); }
  .card--back .wordmark__name { font-size: 64px; }

  .person {
    position: absolute;
    right: 58px;
    top: 56px;
    text-align: right;
    font-family: "Playfair Display", serif;
  }
  .person__name { font-size: 30px; font-weight: 700; color: var(--bronze); }
  .person__role { font-size: 22px; color: var(--bronze-soft); margin-top: 2px; }

  .contacts {
    position: absolute;
    left: 484px;
    top: 184px;
    list-style: none;
    color: var(--bronze);
    font-size: 19px;
  }
  .contacts li {
    display: flex;
    align-items: flex-start;
    gap: 18px;
    margin-bottom: 14px;
    line-height: 1.3;
  }
  .contacts .icon {
    width: 20px; height: 20px; flex: none; margin-top: 2px;
    fill: var(--bronze);
    font-size: 19px; text-align: center; line-height: 20px;
  }

  .social-band {
    position: absolute;
    left: 0; right: 0; bottom: 0;
    height: 103px;
    background: var(--sand);
    display: flex;
    align-items: center;
    padding-left: 158px;
    gap: 118px;
  }
  .social {
    display: flex;
    align-items: center;
    gap: 10px;
    color: var(--white);
    font-size: 19px;
  }
  .social__dot {
    width: 14px; height: 14px;
    border-radius: 50%;
    background: var(--white);
  }
</style>
</head>
<body>

  <section class="card card--front" aria-label="Card front">
    <div class="wordmark">
      <span class="wordmark__name">Lumarra</span>
      <span class="wordmark__place">ALDER VALE</span>
    </div>
  </section>

  <section class="card card--back" aria-label="Card back">
    <div class="wordmark">
      <span class="wordmark__name">Lumarra</span>
      <span class="wordmark__place">ALDER VALE</span>
    </div>

    <div class="person">
      <p class="person__name">Name of person</p>
      <p class="person__role">Hair Stylist</p>
    </div>

    <ul class="contacts">
      <li>
        <svg class="icon" viewBox="0 0 24 24" aria-hidden="true"><path d="M6.6 10.8c1.4 2.8 3.8 5.1 6.6 6.6l2.2-2.2c.3-.3.7-.4 1-.2 1.1.4 2.3.6 3.6.6.6 0 1 .4 1 1V20c0 .6-.4 1-1 1C10.6 21 3 13.4 3 4c0-.6.4-1 1-1h3.5c.6 0 1 .4 1 1 0 1.3.2 2.5.6 3.6.1.3 0 .7-.2 1l-2.3 2.2z"/></svg>
        <span>+00 01 5550 17</span>
      </li>
      <li>
        <span class="icon" aria-hidden="true">@</span>
        <span>info@lumarrastudio-example.com</span>
      </li>
      <li>
        <svg class="icon" viewBox="0 0 24 24" aria-hidden="true"><path d="M12 2C8.1 2 5 5.1 5 9c0 5.2 7 13 7 13s7-7.8 7-13c0-3.9-3.1-7-7-7zm0 9.5c-1.4 0-2.5-1.1-2.5-2.5S10.6 6.5 12 6.5s2.5 1.1 2.5 2.5-1.1 2.5-2.5 2.5z"/></svg>
        <span>6128<br>N.Corbel Ridge Blvd Alder Vale ,<br>AV 00417</span>
      </li>
      <li>
        <svg class="icon" viewBox="0 0 24 24" aria-hidden="true"><path d="M12 3a9 9 0 1 0 0 18 9 9 0 0 0 0-18zm6.9 8h-3c-.1-2.2-.6-4.2-1.4-5.6A7 7 0 0 1 18.9 11zM12 5c.9 1 1.8 3.1 1.9 6h-3.8C10.2 8.1 11.1 6 12 5zM9.5 5.4C8.7 6.8 8.2 8.8 8.1 11h-3a7 7 0 0 1 4.4-5.6zM5.1 13h3c.1 2.2.6 4.2 1.4 5.6A7 7 0 0 1 5.1 13zM12 19c-.9-1-1.8-3.1-1.9-6h3.8c-.1 2.9-1 5-1.9 6zm2.5-.4c.8-1.4 1.3-3.4 1.4-5.6h3a7 7 0 0 1-4.4 5.6z"/></svg>
        <span>www.lumarrastudio-example.com</span>
      </li>
    </ul>

    <div class="social-band">
      <p class="social" aria-label="Friendvale"><span class="social__dot"></span>@lumarrastudioexample</p>
      <p class="social" aria-label="Pictogrid"><span class="social__dot"></span>@lumarrastudioexample</p>
    </div>
  </section>

</body>
</html>
```